Redesign of iOS App Lumo Tutor

Redesign of existing App Lumo Tutor, an app that helps learning Japanese Kanjis, Hiragana, Katakana.

The functionallity should remain the same as today: the app is free, you may download it at the app store. But: I like the design of my other apps better ;)

Target Market(s)

Students learning Japanese

Industry/Entity Type

Teacher

Font styles to use
Sans Serif

Requirements
Must have
• Lumo Tutor has 7 main screens, all screens has to be designed for iPhone and iPad: Main, Settings, Reading Tests, Writing Tests, Game, Paper Mode, Search
Nice to have
• I like the logo as it is today

```html
<!DOCTYPE html>
<html lang="en">
<head>
<meta charset="utf-8">
<title>Lumo Tutor – Writing Test</title>
<link href="https://fonts.googleapis.com/css2?family=Inter:wght@400;500;600&family=Noto+Sans+JP:wght@300;400&display=swap" rel="stylesheet">
<style>
  :root{
    --page:#f3f3f3;
    --status:#000000;
    --status-text:#ffffff;
    --wood-light:#b98550;
    --wood-mid:#a06c3a;
    --wood-dark:#7a4d26;
    --nav:#b07c47;
    --nav-edge:#8a5a2e;
    --tile:#a7733f;
    --tile-edge:#7d5128;
    --label:#f4e6d4;
    --value:#ffffff;
    --wrong:#c8232b;
    --correct:#4fb534;
    --card:#fbfbfb;
    --card-shade:#ececec;
    --word:#7a3e12;
    --reading:#8a8a8a;
    --pad:#ffffff;
    --grid:#e4e4e4;
    --glyph:#dcdcdc;
    --button-text:#9a5a24;
  }
  *{box-sizing:border-box;margin:0;padding:0}
  html,body{width:1000px;height:1200px;overflow:hidden;background:var(--page)}
  body{font-family:"Inter",Helvetica,Arial,sans-serif;position:relative}
  .screen{position:absolute;left:180px;top:32px;width:640px;height:1136px;overflow:hidden;background:var(--wood-mid)}
  .wood{position:absolute;inset:0;background:
      linear-gradient(90deg,var(--wood-dark) 0%,var(--wood-light) 6%,var(--wood-mid) 20%,var(--wood-light) 35%,var(--wood-mid) 50%,var(--wood-light) 65%,var(--wood-mid) 80%,var(--wood-light) 94%,var(--wood-dark) 100%)}
  .status-bar{position:absolute;left:0;top:0;width:640px;height:48px;background:var(--status);color:var(--status-text);font-size:19px;font-weight:500}
  .status-bar .carrier{position:absolute;left:14px;top:13px;display:flex;align-items:center;gap:6px}
  .status-bar .time{position:absolute;left:0;right:0;top:13px;text-align:center;font-weight:600}
  .status-bar .battery{position:absolute;right:12px;top:12px;display:flex;align-items:center;gap:8px}
  .nav-bar{position:absolute;left:0;top:48px;width:640px;height:76px;background:var(--nav);border-bottom:2px solid var(--nav-edge);box-shadow:0 3px 6px rgba(0,0,0,.3)}
  .nav-bar .menu-button{position:absolute;left:28px;top:15px;width:64px;height:42px;background:var(--tile);border-radius:3px;box-shadow:inset 0 0 0 1px var(--tile-edge)}
  .nav-bar .menu-button svg{position:absolute;left:18px;top:9px}
  .nav-bar h1{position:absolute;left:0;right:0;top:18px;text-align:center;font-weight:400;font-size:32px;color:#fff;text-shadow:0 1px 2px rgba(0,0,0,.4)}
  .stats{position:absolute;left:37px;top:163px;display:flex;gap:9px}
  .stat{width:135px;height:107px;background:var(--tile);border-radius:3px;box-shadow:inset 0 0 0 1px var(--tile-edge),0 2px 4px rgba(0,0,0,.35);text-align:center;padding-top:18px}
  .stat .label{font-size:19px;color:var(--label);display:block}
  .stat .value{font-size:46px;line-height:52px;color:var(--value);display:block;font-weight:400}
  .stat .value.wrong{color:var(--wrong)}
  .stat .value.correct{color:var(--correct)}
  .word-card{position:absolute;left:37px;top:296px;width:566px;height:143px;background:linear-gradient(var(--card),var(--card-shade));text-align:center;box-shadow:0 2px 4px rgba(0,0,0,.3)}
  .word-card .meaning{font-size:50px;font-weight:600;color:var(--word);margin-top:26px;line-height:56px}
  .word-card .reading{font-family:"Noto Sans JP",sans-serif;font-size:22px;color:var(--reading);font-weight:300}
  .writing-pad{position:absolute;left:37px;top:458px;width:566px;height:567px;background:var(--pad)}
  .writing-pad .guide-v{position:absolute;left:282px;top:0;width:1px;height:100%;background:var(--grid)}
  .writing-pad .guide-h{position:absolute;top:283px;left:0;height:1px;width:100%;background:var(--grid)}
  .writing-pad .kanji{position:absolute;left:0;right:0;top:30px;text-align:center;font-family:"Noto Sans JP",sans-serif;font-weight:400;font-size:470px;line-height:520px;color:var(--glyph)}
  .progress{position:absolute;left:35px;top:1061px;font-size:23px;font-weight:500;color:#fff;text-shadow:0 1px 2px rgba(0,0,0,.4)}
  .next-button{position:absolute;left:435px;top:1043px;width:168px;height:62px;background:linear-gradient(#ffffff,#ededed);box-shadow:0 2px 4px rgba(0,0,0,.3);display:flex;align-items:center;justify-content:center;gap:18px;font-size:24px;font-weight:500;color:var(--button-text)}
</style>
</head>
<body>
<main class="screen">
  <div class="wood" role="img" aria-label="Wooden plank background texture"></div>

  <header class="status-bar">
    <div class="carrier">
      <span>●●●●●</span><span>NOVA</span>
      <svg width="20" height="15" viewBox="0 0 20 15"><path d="M1 5a13 13 0 0 1 18 0M4 8.5a8.5 8.5 0 0 1 12 0M7 12a4 4 0 0 1 6 0" stroke="#fff" stroke-width="2" fill="none" stroke-linecap="round"/></svg>
    </div>
    <div class="time">4:21 PM</div>
    <div class="battery">
      <svg width="12" height="20" viewBox="0 0 12 20"><path d="M1 6l9 8-4.5 4V2L10 6 1 14" stroke="#bbb" stroke-width="1.6" fill="none"/></svg>
      <span>100%</span>
      <svg width="42" height="20" viewBox="0 0 42 20"><rect x="1" y="2" width="36" height="16" rx="3" fill="#fff"/><rect x="38" y="7" width="3" height="6" rx="1" fill="#fff"/></svg>
    </div>
  </header>

  <nav class="nav-bar">
    <div class="menu-button">
      <svg width="28" height="24" viewBox="0 0 28 24" fill="#fff"><rect x="0" y="1" width="4" height="4"/><rect x="6" y="1" width="22" height="4"/><rect x="0" y="10" width="4" height="4"/><rect x="6" y="10" width="22" height="4"/><rect x="0" y="19" width="4" height="4"/><rect x="6" y="19" width="22" height="4"/></svg>
    </div>
    <h1>Writting Test</h1>
  </nav>

  <section class="stats">
    <div class="stat"><span class="label">Level</span><span class="value">1</span></div>
    <div class="stat"><span class="label">Remaining</span><span class="value">102</span></div>
    <div class="stat"><span class="label">Wrong</span><span class="value wrong">1</span></div>
    <div class="stat"><span class="label">Correct</span><span class="value correct">102</span></div>
  </section>

  <section class="word-card">
    <p class="meaning">fire</p>
    <p class="reading">か, ひ</p>
  </section>

  <section class="writing-pad">
    <div class="guide-v"></div>
    <div class="guide-h"></div>
    <div class="kanji" lang="ja">火</div>
  </section>

  <p class="progress">1 of 102 tests</p>
  <div class="next-button">
    <span>NEXT</span>
    <svg width="22" height="32" viewBox="0 0 22 32"><path d="M4 3l14 13L4 29" stroke="#a8612a" stroke-width="7" fill="none" stroke-linecap="round" stroke-linejoin="round"/></svg>
  </div>
</main>
</body>
</html>
```